Sunmeadow Home Care Business Card

We are a home care company customizing in personal care services. Our personal care service is different because our mission is to provide the most effective care while enhancing quality of life. We strive to make everyday our client's best day. I would like a very classic and/or retro feel. I don't like clip art.

Target Market(s)

doctor's offices; potential clients

Industry/Entity Type

Business

Contact Information for Business Card

jdalton@sunmeadowhc.example(919) 480-15904000 Blue Ridge Road, Suite 101Raleigh, NC 27612www.SunmeadowHC.example

Requirements
Must have
• classic and/or retro feel. Very caring.
Should not have
• Clip art

```html
<!DOCTYPE html>
<html lang="en">
<head>
<meta charset="utf-8">
<title>Sunmeadow Home Care – Business Card</title>
<link rel="stylesheet" href="https://fonts.googleapis.com/css2?family=Arimo:wght@400;700&display=swap">
<style>
  :root {
    --page-bg: #e9e6e1;
    --card-white: #ffffff;
    --card-black: #141414;
    --brand-blue: #1b8fd8;
    --brand-green: #5fb533;
    --text-light: #f2f2f2;
    --icon-blue: #2a9ae0;
  }
  * { margin: 0; padding: 0; box-sizing: border-box; }
  html, body {
    width: 1200px; height: 1024px; overflow: hidden;
    background: var(--page-bg);
    font-family: "Arimo", Arial, sans-serif;
  }
  .card {
    position: absolute; left: 250px; width: 700px; height: 400px;
    border-radius: 4px; overflow: hidden;
    box-shadow: 0 10px 28px rgba(0,0,0,0.22);
  }
  .card--front { top: 80px; background: var(--card-white); }
  .card--back {
    top: 544px;
    background: radial-gradient(ellipse at 45% 40%, #2e2e2e 0%, var(--card-black) 70%);
  }
  .card__art { position: absolute; inset: 0; width: 100%; height: 100%; }
  .brand-name {
    position: absolute; color: var(--brand-blue);
    font-weight: 700; line-height: 1.1; letter-spacing: 0.3px;
  }
  .card--front .brand-name { left: 36px; top: 106px; font-size: 28px; }
  .card--back .brand-name {
    left: 0; right: 0; top: 140px; text-align: center; font-size: 50px;
  }
  .contact {
    position: absolute; list-style: none; color: var(--text-light);
    font-size: 14px; line-height: 1.35;
  }
  .contact li { display: flex; align-items: flex-start; gap: 10px; margin-bottom: 6px; }
  .contact svg { flex: none; width: 14px; height: 14px; margin-top: 2px; }
  .contact--left { left: 40px; top: 322px; }
  .contact--right { left: 440px; top: 52px; }
</style>
</head>
<body>

<section class="card card--front" aria-label="Business card front">
  <svg class="card__art" viewBox="0 0 700 400" aria-hidden="true">
    <path d="M470,0 C380,50 350,180 250,245 C170,295 80,302 0,302"
          fill="none" stroke="var(--brand-blue)" stroke-width="6" transform="translate(-16,-14)"/>
    <path d="M470,0 C380,50 350,180 250,245 C170,295 80,302 0,302 L0,400 L700,400 L700,0 Z"
          fill="var(--brand-green)"/>
    <path d="M490,0 C400,56 370,192 262,258 C180,310 85,316 0,316 L0,386 L686,386 L686,0 Z"
          fill="var(--card-black)"/>
  </svg>

  <div class="brand-name">Sunmeadow<br>Home Care, Inc.</div>

  <ul class="contact contact--left">
    <li>
      <svg viewBox="0 0 14 14"><path d="M3 1 L5 4 L4 5.5 C5 8 6 9 8.5 10 L10 9 L13 11 L11.5 13 C6 12.5 1.5 8 1 2.5 Z" fill="var(--icon-blue)"/></svg>
      <span>(555) 302-7741</span>
    </li>
    <li>
      <svg viewBox="0 0 14 14"><path d="M7 1 C4.2 1 2.5 3 2.5 5.3 C2.5 8.5 7 13 7 13 C7 13 11.5 8.5 11.5 5.3 C11.5 3 9.8 1 7 1 Z" fill="var(--icon-blue)"/><circle cx="7" cy="5.3" r="1.7" fill="var(--card-black)"/></svg>
      <span>2700 Copper Finch Lane, Suite 101<br>Larkfield, NC 27599</span>
    </li>
  </ul>

  <ul class="contact contact--right">
    <li>
      <svg viewBox="0 0 14 14"><rect x="1" y="3" width="12" height="8" rx="1" fill="var(--icon-blue)"/><path d="M1.5 3.5 L7 8 L12.5 3.5" fill="none" stroke="var(--card-black)" stroke-width="1.2"/></svg>
      <span>jdalton@sunmeadowhc.example</span>
    </li>
    <li>
      <svg viewBox="0 0 14 14"><circle cx="7" cy="7" r="6" fill="none" stroke="var(--icon-blue)" stroke-width="1.4"/><ellipse cx="7" cy="7" rx="2.6" ry="6" fill="none" stroke="var(--icon-blue)" stroke-width="1.2"/><path d="M1 7 H13" stroke="var(--icon-blue)" stroke-width="1.2"/></svg>
      <span>www.SunmeadowHC.example</span>
    </li>
  </ul>
</section>

<section class="card card--back" aria-label="Business card back">
  <div class="brand-name">Sunmeadow<br>Home Care, Inc.</div>
</section>

</body>
</html>
```